Business Card Design for Real Estate Company

I am looking for a business card design that will catch my client's attention.

Industry/Entity Type

Business

Requirements
Must have
• Please have the following information in the business card design. You can substitute the "Office, Mobile, email, and web" with an icon or some other design you may think will go well with the business card.

Derek Osmund
482 W. Fenwick St., Suite 310
Pasadena, CA 91348
Office: 626.748.1196
Mobile: 626.913.4071
email: Derek@CrestviewPropertyWalk.example
web: www.CrestviewPropertyWalk.example

```html
<!DOCTYPE html>
<html lang="en">
<head>
<meta charset="utf-8">
<title>Crestview Property Walk – Business Card</title>
<link rel="stylesheet" href="https://fonts.googleapis.com/css2?family=Tinos&display=swap">
<style>
  :root {
    --paper: #ffffff;
    --brown: #3c2a20;
    --blue: #1f80c4;
    --icon-blue: #2290d8;
    --mark-green: #7cb342;
    --mark-yellow: #f2b318;
    --mark-blue: #2a8fd4;
    --light: #ffffff;
  }
  * { margin: 0; padding: 0; box-sizing: border-box; }
  html, body {
    width: 751px;
    height: 1200px;
    overflow: hidden;
    background: var(--paper);
  }
  .card {
    position: relative;
    width: 751px;
    height: 1200px;
    background: var(--paper);
    font-family: "Tinos", "Times New Roman", serif;
  }
  .company {
    position: absolute;
    top: 40px;
    left: 0;
    width: 100%;
    text-align: center;
    color: var(--brown);
    font-weight: 400;
    line-height: 1;
  }
  .company-line1 {
    display: block;
    font-size: 66px;
    letter-spacing: 1px;
  }
  .company-line2 {
    display: block;
    margin-top: 36px;
    font-size: 47px;
    letter-spacing: 1px;
  }
  .brand-mark {
    position: absolute;
    top: 400px;
    left: 225px;
    width: 300px;
    height: 380px;
    background: linear-gradient(120deg, var(--mark-green) 0%, var(--mark-yellow) 45%, var(--mark-blue) 100%);
    opacity: 0.85;
  }
  .agent-name {
    position: absolute;
    top: 842px;
    left: 0;
    width: 100%;
    text-align: center;
    color: var(--blue);
    font-size: 32px;
    letter-spacing: 0.5px;
    font-weight: 400;
  }
  .contact-band {
    position: absolute;
    left: 0;
    top: 915px;
    width: 100%;
    height: 285px;
    background: var(--brown);
    color: var(--light);
    font-size: 31px;
    line-height: 1.3;
  }
  .contact-row {
    position: absolute;
    left: 16px;
    display: flex;
    align-items: flex-start;
  }
  .contact-row .icon {
    width: 44px;
    flex: none;
    fill: var(--icon-blue);
  }
  .contact-row .text { margin-left: 14px; }
  .row-address { top: 26px; }
  .row-address .icon { margin-top: -2px; }
  .row-mobile { top: 128px; }
  .row-mobile .icon { width: 30px; margin-left: 7px; margin-right: 7px; }
  .row-email { top: 172px; }
  .row-email .icon { margin-top: 9px; }
  .row-web { top: 216px; }
  .row-web .icon { margin-top: 4px; width: 40px; margin-left: 2px; margin-right: 2px; }
</style>
</head>
<body>
<main class="card">
  <h1 class="company">
    <span class="company-line1">CRESTVIEW</span>
    <span class="company-line2">PROPERTY WALK</span>
  </h1>

  <div class="brand-mark" role="img" aria-label="Company brand mark area"></div>

  <p class="agent-name">DEREK OSMUND</p>

  <section class="contact-band">
    <div class="contact-row row-address">
      <svg class="icon" viewBox="0 0 44 44" aria-label="Office">
        <path d="M22 3 L42 21 H36 V42 H26 V29 H18 V42 H8 V21 H2 Z"/>
      </svg>
      <p class="text">482 W. Fenwick St., Suite 310 Pasadena<br>CA 91348 - 626.748.1196</p>
    </div>
    <div class="contact-row row-mobile">
      <svg class="icon" viewBox="0 0 30 46" aria-label="Mobile">
        <rect x="2" y="2" width="26" height="42" rx="5"/>
        <rect x="6" y="8" width="18" height="18" fill="#3c2a20"/>
        <circle cx="15" cy="35" r="3" fill="#3c2a20"/>
      </svg>
      <p class="text">626.913.4071</p>
    </div>
    <div class="contact-row row-email">
      <svg class="icon" viewBox="0 0 44 30" aria-label="Email">
        <rect x="2" y="2" width="40" height="26" fill="none" stroke="#2290d8" stroke-width="3"/>
        <path d="M2 2 L22 17 L42 2" fill="none" stroke="#2290d8" stroke-width="3"/>
      </svg>
      <p class="text">Derek@CrestviewPropertyWalk.example</p>
    </div>
    <div class="contact-row row-web">
      <svg class="icon" viewBox="0 0 40 40" aria-label="Web">
        <g fill="none" stroke="#2290d8" stroke-width="3">
          <circle cx="20" cy="20" r="17"/>
          <ellipse cx="20" cy="20" rx="7" ry="17"/>
          <path d="M3 20 H37"/>
        </g>
      </svg>
      <p class="text">www.CrestviewPropertyWalk.example</p>
    </div>
  </section>
</main>
</body>
</html>
```